Designing Forms for Brightledger

I need to create professional forms that can be edited in Microsoft Word. 1. I would like the forms to include our logo (see upload). I have this logo as a PDF, JPG, or source file (.ZIP). I would like the logo to be blue.2. I would like the forms to be readable from top to bottom of the page when viewing in portrait layout, not landscape layout. 3. I have included samples of the forms I have created. Some of them are in landscape mode and need to be changed. The text in the information cells are just examples so you can see what will be used as inputs, but the forms should not have data on them except for the titles and column headers. 4. There are 6 different forms.

Target Market(s)

Individuals and families

Industry/Entity Type

Financial Planning

Requirements
Must have
• Logo
• Portrait layout

```html
<!DOCTYPE html>
<html lang="en">
<head>
<meta charset="utf-8">
<title>My Charitable Donations – Form</title>
<link rel="stylesheet" href="https://fonts.googleapis.com/css2?family=Noto+Serif:wght@400;700&family=Open+Sans:wght@400;700&display=swap">
<style>
  :root {
    --backdrop: #454545;
    --paper: #ffffff;
    --ink: #333a40;
    --band-light: #9dd9f5;
    --band-deep: #2ba6df;
    --footer-light: #5cc0ec;
    --footer-deep: #6d9fd8;
    --header-cell: #5bbfea;
    --header-text: #34475a;
    --grid-line: #a7cdee;
    --on-band: #ffffff;
  }
  * { box-sizing: border-box; margin: 0; padding: 0; }
  html, body {
    width: 1200px; height: 1200px; overflow: hidden;
    background: var(--backdrop);
  }
  .form-page {
    position: absolute;
    left: 196px; top: 30px;
    width: 807px; height: 1140px;
    background: var(--paper);
    overflow: hidden;
  }
  .header-band {
    position: absolute;
    left: 0; top: 0;
    width: 100%; height: 128px;
    background: linear-gradient(90deg, var(--band-light) 0%, var(--band-deep) 100%);
  }
  .footer-band {
    position: absolute;
    left: 0; bottom: 0;
    width: 100%; height: 58px;
    background: linear-gradient(90deg, var(--footer-light) 0%, var(--footer-deep) 100%);
  }
  .form-title {
    position: absolute;
    left: 45px; top: 36px;
    font-family: "Noto Serif", serif;
    font-weight: 700;
    font-size: 37px;
    line-height: 39px;
    letter-spacing: 2px;
    color: var(--ink);
  }
  .brand-name {
    position: absolute;
    right: 40px; top: 50px;
    font-family: "Noto Serif", serif;
    font-weight: 400;
    font-size: 20px;
    letter-spacing: 1px;
    color: var(--on-band);
  }
  .donation-log {
    position: absolute;
    left: 58px; top: 147px;
    width: 709px;
    border-collapse: collapse;
    table-layout: fixed;
    font-family: "Open Sans", sans-serif;
  }
  .donation-log th {
    height: 33px;
    background: var(--header-cell);
    color: var(--header-text);
    font-weight: 400;
    font-size: 14px;
    border: 1px solid var(--grid-line);
  }
  .donation-log td {
    height: 32.5px;
    border: 1px solid var(--grid-line);
  }
  .col-date { width: 94px; }
  .col-org { width: 230px; }
  .col-items { width: 262px; }
  .col-amount { width: 123px; }
  .page-number {
    position: absolute;
    right: 38px; bottom: 16px;
    font-family: "Open Sans", sans-serif;
    font-size: 14px;
    color: var(--on-band);
  }
  .page-number strong { font-weight: 700; }
</style>
</head>
<body>
  <main class="form-page">
    <div class="header-band" role="img" aria-label="Flowing blue wave header decoration"></div>
    <div class="footer-band" role="img" aria-label="Flowing blue wave footer decoration"></div>

    <h1 class="form-title">MY CHARITABLE<br>DONATIONS</h1>
    <div class="brand-name">BRIGHTLEDGER</div>

    <table class="donation-log">
      <colgroup>
        <col class="col-date"><col class="col-org"><col class="col-items"><col class="col-amount">
      </colgroup>
      <thead>
        <tr><th>DATE</th><th>ORGANIZATION</th><th>ITEMS</th><th>AMOUNT</th></tr>
      </thead>
      <tbody>
        <tr><td></td><td></td><td></td><td></td></tr>
        <tr><td></td><td></td><td></td><td></td></tr>
        <tr><td></td><td></td><td></td><td></td></tr>
        <tr><td></td><td></td><td></td><td></td></tr>
        <tr><td></td><td></td><td></td><td></td></tr>
        <tr><td></td><td></td><td></td><td></td></tr>
        <tr><td></td><td></td><td></td><td></td></tr>
        <tr><td></td><td></td><td></td><td></td></tr>
        <tr><td></td><td></td><td></td><td></td></tr>
        <tr><td></td><td></td><td></td><td></td></tr>
        <tr><td></td><td></td><td></td><td></td></tr>
        <tr><td></td><td></td><td></td><td></td></tr>
        <tr><td></td><td></td><td></td><td></td></tr>
        <tr><td></td><td></td><td></td><td></td></tr>
        <tr><td></td><td></td><td></td><td></td></tr>
        <tr><td></td><td></td><td></td><td></td></tr>
        <tr><td></td><td></td><td></td><td></td></tr>
        <tr><td></td><td></td><td></td><td></td></tr>
        <tr><td></td><td></td><td></td><td></td></tr>
        <tr><td></td><td></td><td></td><td></td></tr>
        <tr><td></td><td></td><td></td><td></td></tr>
        <tr><td></td><td></td><td></td><td></td></tr>
        <tr><td></td><td></td><td></td><td></td></tr>
        <tr><td></td><td></td><td></td><td></td></tr>
        <tr><td></td><td></td><td></td><td></td></tr>
        <tr><td></td><td></td><td></td><td></td></tr>
        <tr><td></td><td></td><td></td><td></td></tr>
      </tbody>
    </table>

    <p class="page-number">Page <strong>1</strong> of <strong>1</strong></p>
  </main>
</body>
</html>
```